依頼詳細
「企業ロゴ」が黒と黄色のため、基本的なカラーリングベースは、黒色で黄色のあしらいやワンポイントカラーを入れるイメージを持っております。
デザインイメージは、「未来的」「先進的」などを強く主張したいと思っております。

本件は、Topページのみのテストとして、「コンペ形式」となりますが、
当選された場合には、約10ページほどの下層ページのご依頼も約束させて頂きます。
(予算は10万円前後)
さらに、今後の案件にて、「継続的」に案件を斡旋させて頂きたいと思っておりますので、
末長くお付き合いして頂けると幸いです。
また、当選後は、デザインに利用したファイルやデータを提出して頂きたいです。

```html
<!DOCTYPE html>
<html lang="en">
<head>
<meta charset="utf-8">
<title>Farhold — Create the future</title>
<link href="https://fonts.googleapis.com/css2?family=Roboto:wght@700;900&display=swap" rel="stylesheet">
<style>
  :root {
    --bg: #231a17;
    --white: #ffffff;
    --accent: #f5dd2a;
    --gold-light: #e6d83a;
    --gold-mid: #c9ba1f;
    --gold-deep: #a8901a;
    --ink: #231a17;
  }
  html, body {
    margin: 0;
    padding: 0;
    width: 1200px;
    height: 2596px;
    overflow: hidden;
    background: var(--bg);
  }
  .page {
    position: relative;
    width: 1200px;
    height: 2596px;
    background: var(--bg);
    font-family: "Roboto", Arial, sans-serif;
  }
  .brand {
    position: absolute;
    left: 48px;
    top: 92px;
    margin: 0;
    color: var(--white);
    font-weight: 700;
    font-size: 104px;
    line-height: 1;
    letter-spacing: -1px;
  }
  .contact-button {
    position: absolute;
    left: 976px;
    top: 56px;
    width: 176px;
    height: 176px;
    border-radius: 50%;
    background: var(--accent);
    display: flex;
    align-items: center;
    justify-content: center;
  }
  .headline {
    position: absolute;
    right: 88px;
    top: 430px;
    margin: 0;
    text-align: right;
    font-weight: 700;
    font-size: 190px;
    line-height: 232px;
    letter-spacing: -1px;
    background: linear-gradient(100deg, var(--gold-mid), var(--gold-light) 45%, var(--gold-deep) 80%, var(--gold-light));
    -webkit-background-clip: text;
    background-clip: text;
    color: transparent;
  }
  .hero-art {
    position: absolute;
    left: 32px;
    top: 1328px;
    width: 1120px;
    height: 1232px;
    background: linear-gradient(160deg, #d9b52a 0%, #f0d43a 35%, #c8951c 65%, #e6c23a 100%);
    opacity: 0.92;
  }
</style>
</head>
<body>
  <main class="page">
    <p class="brand">Farhold</p>

    <a class="contact-button" aria-label="Contact">
      <svg width="84" height="84" viewBox="0 0 24 24" fill="none" stroke="var(--ink)" stroke-width="1.8" stroke-linejoin="round" stroke-linecap="round">
        <path d="M22 2 2 9.5l8 3.5 3.5 8L22 2z"/>
        <path d="M22 2 10 13"/>
      </svg>
    </a>

    <h1 class="headline">Create<br>the future<br>to<br>Farhold</h1>

    <div class="hero-art" role="img" aria-label="Golden silhouette of a howling wolf with a marbled gold texture"></div>
  </main>
</body>
</html>
```